K.D.L.R.C. Soccer Tryouts 2015-2016

I am looking for a soccer tryout flyer that stands out and catches peoples attention. An emphasis can be put on the cost, since we are by far the lowest cost program in the area. Below are the details for the flyer. I have also attached the club logo and pictures that can be used if needed.

K.D.L.R.C. SOCCER TRYOUTS
2015-2016

Club Fee: $699.00 per player

Tryout Schedule

Boys ages U9 through U14
Weds. May 27th and Friday May 29th
6:00 pm - 8:00 pm

Girls ages U9 through U14
Tuesday May 26th and Thursday May 28th
6:00 pm - 8:00 pm

All tryouts will be held at TPRA Fields
(Next to Brightmark Gear factory at the corner of Rt. 482 and Pebble Crest Road)

We are encouraging all players to pre-register

Same Day Registrations will begin at 5:30

All players should bring a properly inflated ball, shin guards and water.

In the event of inclement weather, the tryouts will be moved to the QRT indoor facility located at 2874 Thornmoor Road in Maple Hollow. The scheduled time slots will remain the same.

Website: www.kdlrc-example.com

Target Market(s)

Youth Soccer

Requirements
Must have
• Logo

```html
<!DOCTYPE html>
<html lang="en">
<head>
<meta charset="utf-8">
<title>K.D.L.R.C. Soccer Tryouts 2015-2016</title>
<link href="https://fonts.googleapis.com/css2?family=Russo+One&family=Roboto+Condensed:wght@400;700&display=swap" rel="stylesheet">
<style>
  :root {
    --page-bg: #d9d9d9;
    --paper: #f4f4f4;
    --purple: #5a2a82;
    --olive: #3f5a12;
    --lime-text: #b7e83a;
    --red: #c8101a;
    --dark: #1f1f1f;
    --ink: #222;
  }
  * { box-sizing: border-box; margin: 0; padding: 0; }
  html, body { width: 907px; height: 1200px; overflow: hidden; }
  body { background: var(--page-bg); position: relative; font-family: "Roboto Condensed", sans-serif; }

  .flyer {
    position: absolute; left: 46px; top: 30px; width: 814px; height: 1140px;
    background: var(--paper); overflow: hidden;
    box-shadow: 0 4px 14px rgba(0,0,0,.25);
  }
  .team-photo {
    position: absolute; left: 0; top: 0; width: 814px; height: 450px;
    background: linear-gradient(180deg, #5f6f34 0%, #8a8a52 30%, #7a9c6a 55%, #6f9fc2 68%, #4f7a3a 100%);
  }
  .backdrop-photo {
    position: absolute; left: 0; top: 640px; width: 814px; height: 420px;
    background: linear-gradient(180deg, #e8e8e8 0%, #cfcfcf 50%, #e4e4e4 100%);
  }
  .swoosh { position: absolute; left: 0; top: 280px; width: 814px; height: 360px; }

  .club-badge {
    position: absolute; left: 365px; top: 353px; width: 216px; height: 216px;
    border-radius: 50%;
    background: radial-gradient(circle at 40% 35%, #ffffff 0%, #dcdcdc 60%, #a9a9a9 100%);
    box-shadow: 0 4px 10px rgba(0,0,0,.35);
    display: flex; align-items: center; justify-content: center;
  }
  .club-badge span { font-family: "Russo One", sans-serif; font-size: 28px; color: var(--purple); }

  .title {
    position: absolute; left: 0; width: 814px; text-align: center;
    font-family: "Russo One", sans-serif; font-weight: 400;
  }
  .title-main { top: 608px; font-size: 41px; color: var(--purple); letter-spacing: 1px; }
  .title-year { top: 670px; font-size: 41px; color: var(--olive); }
  .rule { position: absolute; left: 38px; top: 729px; width: 740px; height: 2px; background: var(--olive); }

  .schedule-shield { position: absolute; left: 38px; top: 760px; width: 290px; height: 260px; }
  .schedule-text {
    position: absolute; left: 58px; top: 778px; width: 250px; text-align: center;
    color: #fff; font-size: 16px; line-height: 19px;
  }
  .schedule-text h2 {
    font-family: "Russo One", sans-serif; font-weight: 400; font-variant: small-caps;
    color: var(--lime-text); font-size: 21px; line-height: 26px; margin-bottom: 6px;
    text-decoration: underline; text-underline-offset: 3px;
  }
  .schedule-text .group { color: var(--lime-text); }
  .schedule-text .slot { margin-bottom: 9px; }

  .details { position: absolute; left: 383px; top: 764px; width: 400px; color: var(--ink); }
  .details h3 {
    font-family: "Russo One", sans-serif; font-weight: 400; font-variant: small-caps;
    color: var(--olive); font-size: 23px; line-height: 30px;
  }
  .details .note { font-size: 15px; line-height: 17px; margin-top: 2px; }
  .details .encourage { color: var(--purple); font-size: 17.5px; margin-top: 12px; }
  .details .same-day {
    font-family: "Russo One", sans-serif; font-variant: small-caps; color: var(--purple);
    font-size: 23px; line-height: 27px; margin-top: 10px;
  }
  .details .bring { font-size: 15.5px; line-height: 18px; margin-top: 8px; width: 250px; }

  .price {
    position: absolute; left: 647px; top: 927px; width: 134px; height: 134px; border-radius: 50%;
    background: radial-gradient(circle at 45% 35%, #ee2a2a 0%, var(--red) 60%, #8a0a10 100%);
    border: 4px solid #e6e6e6; box-shadow: 0 3px 8px rgba(0,0,0,.35);
    color: #fff; text-align: center; padding-top: 24px;
  }
  .price strong { display: block; font-family: "Russo One", sans-serif; font-weight: 400; font-size: 42px; line-height: 46px; }
  .price small { display: block; font-family: "Russo One", sans-serif; font-size: 15px; color: var(--lime-text); }

  .footer {
    position: absolute; left: 0; top: 1060px; width: 814px; height: 80px; background: var(--dark);
    border-top: 3px solid #bdbdbd;
  }
  .footer .weather {
    position: absolute; left: 26px; top: 12px; width: 560px;
    color: var(--lime-text); font-size: 14.5px; line-height: 18px;
  }
  .footer .site { position: absolute; right: 28px; top: 22px; color: #fff; font-size: 16px; }
</style>
</head>
<body>
  <main class="flyer">
    <div class="team-photo" role="img" aria-label="Team photo of youth girls soccer players in light blue jerseys with their coach on a grass field"></div>
    <div class="backdrop-photo" role="img" aria-label="Faded greyscale team photo in the background"></div>

    <svg class="swoosh" viewBox="0 0 814 360" preserveAspectRatio="none" aria-hidden="true">
      <defs>
        <linearGradient id="limeFill" x1="0" y1="0" x2="1" y2="1">
          <stop offset="0" stop-color="#c7ee6a"/>
          <stop offset="1" stop-color="#7fbf16"/>
        </linearGradient>
      </defs>
      <path d="M0 120 C160 210 300 200 420 175 C560 140 680 60 814 60 L814 360 L0 360 Z" fill="#f4f4f4"/>
      <path d="M0 125 C150 215 300 210 430 180 C570 145 690 70 814 75 L814 310 C700 260 560 230 420 270 C280 310 140 340 0 330 Z" fill="url(#limeFill)"/>
      <path d="M0 145 C150 235 300 225 430 195 C570 160 690 90 814 92" fill="none" stroke="#ffffff" stroke-width="7"/>
      <path d="M0 155 C150 245 300 235 430 205 C570 170 690 100 814 102" fill="none" stroke="#2a3a10" stroke-width="3" opacity=".7"/>
      <path d="M0 330 C140 340 280 310 420 270 C560 230 700 260 814 310 L814 360 L0 360 Z" fill="#f4f4f4"/>
      <path d="M0 330 C140 340 280 310 420 270 C560 230 700 260 814 310" fill="none" stroke="#9ad12a" stroke-width="3"/>
    </svg>

    <div class="club-badge"><span>K.D.L.R.C.</span></div>

    <h1 class="title title-main">K.D.L.R.C. SOCCER TRYOUTS</h1>
    <p class="title title-year">2015-2016</p>
    <div class="rule"></div>

    <svg class="schedule-shield" viewBox="0 0 290 260" aria-hidden="true">
      <defs>
        <linearGradient id="shieldFill" x1="0" y1="0" x2="0" y2="1">
          <stop offset="0" stop-color="#9b3ddb"/>
          <stop offset="1" stop-color="#6a1fa8"/>
        </linearGradient>
      </defs>
      <path d="M10 6 Q145 -6 280 6 L280 160 Q275 220 145 256 Q15 220 10 160 Z" fill="#cfcfcf" stroke="#ffffff" stroke-width="3"/>
      <path d="M20 16 Q145 5 270 16 L270 158 Q265 210 145 244 Q25 210 20 158 Z" fill="url(#shieldFill)"/>
    </svg>
    <div class="schedule-text">
      <h2>Tryout Schedule</h2>
      <div class="slot">
        <div class="group">Boys ages U9 through U14</div>
        <div>Wednesday &amp; Friday</div>
        <div>May 27th &amp; 29th</div>
        <div class="group">6:00 pm - 8:00 pm</div>
      </div>
      <div class="slot">
        <div class="group">Girls ages U9 through U14</div>
        <div>Tuesday &amp; Thursday</div>
        <div>May 26th &amp; 28th</div>
        <div class="group">6:00 pm - 8:00 pm</div>
      </div>
    </div>

    <section class="details">
      <h3>All tryouts will be held at<br>TPRA Fields</h3>
      <p class="note">(Next to Brightmark Gear factory at the corner of Rt. 482 and Pebble Crest Road)</p>
      <p class="encourage">We are encouraging all players to pre-register</p>
      <p class="same-day">Same Day Registrations<br>will begin at 5:30</p>
      <p class="bring">All players should bring a properly inflated ball, shin guards and water</p>
    </section>

    <div class="price"><strong>$699</strong><small>PER PLAYER</small></div>

    <footer class="footer">
      <p class="weather">In the event of inclement weather, the tryouts will be moved to the QRT indoor facility located at 2874 Thornmoor Road in Maple Hollow. The scheduled time slots will remain the same</p>
      <p class="site">www.kdlrc-example.com</p>
    </footer>
  </main>
</body>
</html>
```